Priority Goals poster for school year

We are an elementary school and the past two years have had you help us to design a "poster" that illustrates our goal of the coming year. I am attaching our last year's one, along with some photos of our (ver rough) thinking for next years. The priority goal at top remains the same. Can't wait to see your genius ideas! :)

Target Market(s)

Staff of an elementary school and parents to some (informative) extent as well.

Colors
296eb1
6094c6
fbed22
fbee3f

Requirements
Must have
• items from the white board picture we have attached

```html
<!DOCTYPE html>
<html lang="en">
<head>
<meta charset="utf-8">
<title>Priority Goals Poster</title>
<link rel="stylesheet" href="https://fonts.googleapis.com/css2?family=Poppins:wght@600;700;800&family=Roboto:wght@400;500&family=Oswald:wght@600&display=swap">
<style>
  :root {
    --stage: #3d3d40;
    --paper: #e7eaef;
    --blue: #296eb1;
    --blue-soft: #6094c6;
    --yellow: #fbed22;
    --yellow-soft: #fbee3f;
    --gold: #f3c316;
    --navy: #1e2d6b;
    --ink: #1f2f66;
    --white: #ffffff;
    --band-0: #f3c316;
    --band-1: #f6cf2a;
    --band-2: #fbe25a;
    --band-3: #fbeea5;
    --band-4: #7aa6d8;
    --band-5: #4a80c4;
    --band-6: #2f4f9e;
    --band-7: #1e2d6b;
  }
  * { box-sizing: border-box; margin: 0; padding: 0; }
  html, body { width: 1200px; height: 1200px; overflow: hidden; background: var(--stage); }
  .poster {
    position: absolute; left: 0; top: 176px;
    width: 1200px; height: 848px;
    background: var(--paper);
    font-family: "Roboto", Arial, sans-serif;
    overflow: hidden;
  }
  .poster-shapes { position: absolute; inset: 0; }

  .goal-header { position: absolute; left: 18px; top: 26px; width: 330px; color: var(--white); }
  .goal-year { font-family: "Poppins", Arial, sans-serif; font-weight: 800; font-size: 40px; line-height: 1; color: var(--yellow); letter-spacing: 0.5px; }
  .goal-title { font-family: "Poppins", Arial, sans-serif; font-weight: 700; font-size: 31px; line-height: 1.15; }
  .goal-lede { font-size: 16px; font-weight: 500; line-height: 1.25; margin-top: 8px; width: 285px; }

  .school-name {
    position: absolute; left: 392px; top: 196px; width: 210px;
    font-family: "Poppins", Arial, sans-serif; font-weight: 800;
    font-size: 30px; line-height: 1.05; color: var(--blue); text-align: center;
  }
  .school-name .school-mark {
    display: block; width: 70px; height: 70px; border-radius: 50%;
    background: var(--blue); margin: 0 auto 12px;
  }

  .promise-label {
    position: absolute; left: 43px; top: 480px; width: 278px; text-align: center;
    font-family: "Oswald", Arial Narrow, sans-serif; font-weight: 600;
    font-size: 31px; line-height: 1.1; color: var(--navy); letter-spacing: 0.3px;
  }

  .goal-list { list-style: none; position: absolute; left: 0; top: 0; }
  .goal-item { position: absolute; left: 684px; width: 376px; }
  .goal-item h3 {
    font-family: "Poppins", Arial, sans-serif; font-weight: 600; font-size: 17px;
    line-height: 1.2; color: var(--ink); padding-left: 16px; position: relative;
  }
  .goal-item h3::before { content: "›"; position: absolute; left: 0; top: -2px; font-size: 20px; }
  .goal-item p { font-size: 15px; line-height: 1.25; color: var(--ink); padding-left: 16px; margin-top: 2px; white-space: nowrap; }
  .goal-item p.goal-note-long { font-size: 13.5px; letter-spacing: -0.2px; }
  .goal-item.on-blue h3, .goal-item.on-blue p { color: var(--white); }

  .tagline { position: absolute; left: 44px; top: 700px; display: flex; align-items: center; }
  .tagline-number { font-family: "Poppins", Arial, sans-serif; font-weight: 800; font-size: 112px; line-height: 1; color: var(--gold); margin-right: 16px; }
  .tagline-text { font-family: "Poppins", Arial, sans-serif; font-weight: 800; font-size: 45px; line-height: 1.08; }
  .tagline-text .line-one { color: var(--blue); display: block; }
  .tagline-text .line-two { color: var(--navy); display: block; }
</style>
</head>
<body>
<main class="poster">
  <svg class="poster-shapes" width="1200" height="848" viewBox="0 0 1200 848">
    <defs>
      <filter id="soft-shadow" x="-30%" y="-30%" width="160%" height="160%">
        <feDropShadow dx="0" dy="4" stdDeviation="8" flood-color="#000" flood-opacity="0.15"/>
      </filter>
    </defs>

    <polygon points="0,0 341,0 299,172 0,172" fill="var(--blue)"/>

    <g class="flow-bands">
      <polygon points="288,348 610,348 669,129 1104,129 1104,210 669,210 610,374 288,374" fill="var(--band-0)"/>
      <polygon points="288,374 610,374 669,210 1104,210 1104,291 669,291 610,400 288,400" fill="var(--band-1)"/>
      <polygon points="288,400 610,400 669,291 1104,291 1104,372 669,372 610,426 288,426" fill="var(--band-2)"/>
      <polygon points="288,426 610,426 669,372 1104,372 1104,453 669,453 610,452 288,452" fill="var(--band-3)"/>
      <polygon points="288,452 610,452 669,453 1104,453 1104,534 669,534 610,478 288,478" fill="var(--band-4)"/>
      <polygon points="288,478 610,478 669,534 1104,534 1104,615 669,615 610,504 288,504" fill="var(--band-5)"/>
      <polygon points="288,504 610,504 669,615 1104,615 1104,696 669,696 610,530 288,530" fill="var(--band-6)"/>
      <polygon points="288,530 610,530 669,696 1104,696 1104,777 669,777 610,556 288,556" fill="var(--band-7)"/>
    </g>

    <circle cx="182" cy="447" r="139" fill="var(--white)" filter="url(#soft-shadow)"/>
    <circle cx="182" cy="447" r="124" fill="var(--white)" stroke="#eef0f3" stroke-width="3"/>
    <rect x="142" y="362" width="80" height="70" rx="35" fill="#9fbde0" role="img" aria-label="Heart formed by a handshake icon"/>

    <g class="goal-icons" stroke-width="3" fill="none" stroke-linecap="round" stroke-linejoin="round">
      <circle cx="1104" cy="169" r="38" fill="var(--band-0)" stroke="var(--white)" stroke-width="5"/>
      <g stroke="var(--navy)">
        <path d="M1104 176 l-10 -10 a6 6 0 0 1 10 -7 a6 6 0 0 1 10 7 z"/>
        <path d="M1086 160 v14 l10 12 M1122 160 v14 l-10 12"/>
      </g>
      <circle cx="1104" cy="250" r="38" fill="var(--band-1)" stroke="var(--white)" stroke-width="5"/>
      <g stroke="var(--navy)">
        <circle cx="1104" cy="239" r="8"/>
        <path d="M1088 268 a16 16 0 0 1 32 0 z"/>
      </g>
      <circle cx="1104" cy="331" r="38" fill="var(--band-2)" stroke="var(--white)" stroke-width="5"/>
      <g stroke="var(--navy)">
        <circle cx="1104" cy="331" r="13"/>
        <circle cx="1104" cy="331" r="3" fill="var(--navy)"/>
        <path d="M1104 311 v7 M1104 344 v7 M1084 331 h7 M1117 331 h7"/>
      </g>
      <circle cx="1104" cy="412" r="38" fill="var(--band-3)" stroke="var(--white)" stroke-width="5"/>
      <g stroke="var(--navy)">
        <rect x="1086" y="396" width="16" height="12" rx="2"/>
        <rect x="1106" y="404" width="16" height="12" rx="2"/>
        <path d="M1090 424 h10 M1108 428 h10"/>
      </g>
      <circle cx="1104" cy="493" r="38" fill="var(--band-4)" stroke="var(--white)" stroke-width="5"/>
      <g stroke="var(--white)">
        <circle cx="1096" cy="493" r="9"/>
        <circle cx="1112" cy="493" r="9"/>
      </g>
      <circle cx="1104" cy="574" r="38" fill="var(--band-5)" stroke="var(--white)" stroke-width="5"/>
      <g fill="var(--white)" stroke="none">
        <ellipse cx="1095" cy="570" rx="5" ry="9"/>
        <ellipse cx="1113" cy="580" rx="5" ry="9"/>
      </g>
      <circle cx="1104" cy="655" r="38" fill="var(--band-6)" stroke="var(--white)" stroke-width="5"/>
      <g stroke="var(--white)">
        <path d="M1084 655 q20 -18 40 0 q-20 18 -40 0 z"/>
        <circle cx="1104" cy="655" r="5"/>
      </g>
      <circle cx="1104" cy="736" r="38" fill="var(--band-7)" stroke="var(--white)" stroke-width="5"/>
      <g fill="var(--white)" stroke="none">
        <circle cx="1092" cy="728" r="4"/>
        <circle cx="1104" cy="725" r="5"/>
        <circle cx="1116" cy="728" r="4"/>
        <rect x="1087" y="734" width="10" height="14" rx="3"/>
        <rect x="1098" y="732" width="12" height="18" rx="3"/>
        <rect x="1111" y="734" width="10" height="14" rx="3"/>
      </g>
    </g>

    <rect x="0" y="812" width="553" height="5" fill="var(--gold)"/>
  </svg>

  <header class="goal-header">
    <p class="goal-year">2021-2022</p>
    <h1 class="goal-title">PRIORITY GOALS</h1>
    <p class="goal-lede">We WILL accelerate the academic &amp; social / emotional growth of the students we serve by:</p>
  </header>

  <p class="school-name"><span class="school-mark"></span>LAKEVIEW</p>

  <h2 class="promise-label">FOUNDATIONAL<br>PROMISES</h2>

  <ul class="goal-list">
    <li class="goal-item" style="top:144px"><h3>MENTAL HEALTH &amp; WELLNESS</h3><p>For every person in our community &amp; school</p></li>
    <li class="goal-item" style="top:225px"><h3>STAFF DOING WHAT THEY LOVE</h3><p>Teaching kids for proven growth</p></li>
    <li class="goal-item" style="top:306px"><h3>FOCUS</h3><p>Be intentional with your action</p></li>
    <li class="goal-item" style="top:376px"><h3>COMMUNICATION, COMMUNICATION,<br>COMMUNICATION!</h3><p>Expectations, Support For Clarity</p></li>
    <li class="goal-item on-blue" style="top:468px"><h3>BUILDS &amp; VALUE PARTNERSHIPS</h3><p class="goal-note-long">Connect, Celebrate, Strong, Predictable, Laugh, Have Fun!</p></li>
    <li class="goal-item on-blue" style="top:549px"><h3>SMALL MEASURED STEPS</h3><p>Towards Bigger Goal</p></li>
    <li class="goal-item on-blue" style="top:643px"><h3>BROADEN OUR LENS</h3></li>
    <li class="goal-item on-blue" style="top:711px"><h3>VOICES OF ALL</h3><p>Who are we? Where are we going?</p></li>
  </ul>

  <div class="tagline">
    <span class="tagline-number">4</span>
    <p class="tagline-text"><span class="line-one">YEARS STRONG</span><span class="line-two">BETTER EVERYDAY!</span></p>
  </div>
</main>
</body>
</html>
```